Bloom and Rise Website Design (design layout only)

We need a website design for a new nonprofit organization based in Des Moines, Iowa called Bloom and Rise. The nonprofit provides soccer training opportunities to youth soccer players looking to improve their game while also affecting the lives of the less fortunate in a positive way. While participating in the training programs the players also go out and raise money for selected charities. The organization then donates the funds. In its first 18 months we donated $10,500. We would like to see designs attempt to symbolize the mission of the nonprofit - essentially "improve you while improving someone else."

We would like to see the following features:

· A place to donate - Our intent is to have the home page linked to the donation page; a simple straight-forward process for people to give money, and make donating as painless as possible - no account needed to make a donation, credit card or e-check should be the only information needed to donate, and have it be on a single page.

· A photo gallery so people can browse the photo gallery to get a better understanding of our organization and a place to add videos and a calendar to show upcoming events

· A place for contact information and the profiles of directors and board members. This should include a spot showing all the charities the organization donates to. Also includes a news section/blog for comments and suggestions.

We want the design to revolve around the content and mission. We would really like to stress our organization as nonprofit. We would also like if the website was user friendly and easy to navigate.

The logo of our organization is uploaded

```html
<!DOCTYPE html>
<html lang="en">
<head>
<meta charset="utf-8">
<title>Bloom and Rise</title>
<link rel="stylesheet" href="https://fonts.googleapis.com/css2?family=Questrial&family=Schoolbell&display=swap">
<style>
:root{
  --green:#4e7a35;
  --green-light:#7ea852;
  --green-dark:#3f5f2a;
  --mint:#e4f6c0;
  --olive:#a9b964;
  --footer:#4b5a3a;
  --footer-dark:#2f3a26;
  --orange:#f15a22;
  --yellow:#fdf4a8;
  --ink:#222;
  --white:#fff;
}
*{box-sizing:border-box;margin:0;padding:0}
html,body{width:822px;height:1200px;overflow:hidden;background:#fff}
body{font-family:"Questrial",sans-serif;color:var(--ink)}
.canvas{position:relative;width:822px;height:1200px;overflow:hidden;background:var(--white)}
.abs{position:absolute}

/* header */
.brand{left:42px;top:64px;display:flex;align-items:center;gap:7px}
.brand-mark{width:16px;height:16px;border-radius:50%;background:var(--green)}
.brand-name{font-size:20px;color:var(--green);line-height:1;white-space:nowrap}
.search{left:677px;top:6px;width:106px;height:20px;border:1.5px solid #9aa58f;border-radius:6px;font-size:10px;color:#b0b0b0;padding:3px 0 0 7px}
.search svg{position:absolute;right:6px;top:4px}
.tagline{left:201px;top:58px;font-family:"Schoolbell",cursive;font-size:24px;color:var(--green-dark);letter-spacing:.5px;white-space:nowrap}

/* nav */
.nav{left:31px;top:140px;width:760px;height:36px;background:var(--green)}
.nav-link{position:absolute;top:8px;color:#fff;font-size:16px;white-space:nowrap}
.nav-active{position:absolute;left:195px;top:0;width:101px;height:36px;background:var(--green-light)}
.nav-active span{position:absolute;left:28px;top:8px;color:#fff;font-size:16px;text-decoration:underline}
.donate-btn{left:610px;top:6px;width:77px;height:23px;background:var(--orange);border-radius:2px;text-align:center;font-size:16px;color:#fff;padding-top:2px}
.dropdown{left:226px;top:176px;width:136px;height:53px;background:var(--green-light);z-index:3}
.dropdown div{height:26px;color:#fff;font-size:14px;padding:5px 0 0 33px}
.dropdown .hover{background:var(--green)}

/* hero */
.hero{left:31px;top:181px;width:493px;height:265px;background:linear-gradient(180deg,#b9c6b5 0%,#c9473c 45%,#d8473a 70%,#7e9a4e 100%)}
.hero-caption{left:31px;top:416px;width:493px;height:30px;background:rgba(60,70,40,.55);color:#fff;font-size:16px;padding:5px 0 0 10px;letter-spacing:.4px}
.dots{position:absolute;right:10px;top:9px;display:flex;gap:7px}
.dots i{width:11px;height:11px;border-radius:50%;background:#555;border:1.5px solid #ddd}
.dots i:first-child{background:#fff}

/* donation */
.donation{left:532px;top:181px;width:258px;height:296px;background:var(--green);color:#fff}
.donation h2{font-weight:400;font-size:21px;text-align:center;margin-top:5px}
.field-label{position:absolute;font-size:13px}
.input{position:absolute;background:var(--mint);height:20px}
.select{position:absolute;background:var(--mint);height:20px;color:var(--ink);font-size:14px;padding:1px 0 0 5px}
.select svg{position:absolute;right:4px;top:6px}
.card{position:absolute;top:106px;width:38px;height:23px;background:#fff;border-radius:2px}
.card i{position:absolute;left:6px;top:7px;width:26px;height:9px;border-radius:2px}
.details{position:absolute;left:10px;top:146px;width:238px;height:110px;border:1.5px solid #fff}
.details-title{position:absolute;left:12px;top:-10px;background:var(--green);padding:0 4px;font-size:13px}
.submit{position:absolute;left:0;top:269px;width:100%;text-align:center;font-size:18px}

/* tabs & videos */
.tab{top:454px;height:26px;font-size:16px;padding-top:3px;text-align:center}
.tab-news{left:31px;width:100px;background:var(--green);color:#fff}
.tab-videos{left:131px;width:97px;background:#fff;border:2px solid var(--green);border-bottom:none;color:var(--green-dark)}
.videos{left:31px;top:478px;width:493px;height:173px;border:2px solid var(--green)}
.thumb{position:absolute;top:15px;width:193px;height:135px}
.thumb-a{left:25px;background:linear-gradient(160deg,#9fa89a,#7f9a5a 60%,#6f8f43)}
.thumb-b{left:262px;background:linear-gradient(160deg,#8c9276,#3b3f4a 55%,#6e7650)}
.play{position:absolute;left:76px;top:47px;width:42px;height:42px;border-radius:50%;background:rgba(255,255,255,.85)}
.play svg{position:absolute;left:14px;top:11px}
.more{position:absolute;right:8px;bottom:2px;font-size:11px}

/* events */
.events{left:532px;top:483px;width:258px;height:169px;border:1.5px solid var(--green);padding:5px 0 0 8px;overflow:hidden}
.events h3{font-weight:400;font-size:16px;text-align:center;color:var(--green-dark);margin-bottom:4px}
.event{margin-bottom:7px}
.event small{display:block;font-size:9.5px}
.event p{font-size:12px;color:var(--green-dark)}
.scroll{position:absolute;right:5px;top:6px;width:8px;height:156px}

/* about */
.about{left:31px;top:656px;width:760px;height:178px;background:var(--olive)}
.about-left{left:31px;top:656px;width:11px;height:178px;background:var(--green-dark)}
.about-right{left:779px;top:656px;width:12px;height:178px;background:var(--green-dark)}
.about-text{left:56px;top:674px;width:515px;font-size:13.4px;line-height:18.6px;color:#fff;text-align:justify;letter-spacing:.3px}
.about-text .lead{font-size:18px}
.about-link{left:388px;top:815px;font-size:10.5px;color:#fff;text-decoration:underline}
.portrait{left:623px;top:663px;width:104px;height:134px;background:linear-gradient(180deg,#3a3a3a,#6e6257 60%,#2c2c30)}
.person{left:600px;top:800px;width:150px;text-align:center}
.person b{display:block;font-weight:400;color:var(--orange);font-size:15px}
.person span{font-size:12.5px}

/* charities */
.charities{left:31px;top:842px;width:760px;height:132px;background:var(--yellow);border-radius:16px;overflow:hidden}
.charities h2{height:29px;background:var(--orange);color:#fff;font-weight:400;font-size:17.5px;text-align:center;padding-top:4px}
.charities h2 .hl{color:var(--green-light)}
.charity{position:absolute;top:72px;transform:translateX(-50%);display:flex;align-items:center;gap:5px;font-size:13px;color:var(--green-dark);white-space:nowrap}
.charity i{width:12px;height:12px;border-radius:50%;background:var(--green-light)}
.arrow{position:absolute;top:66px}

/* footer */
.footer{left:31px;top:982px;width:760px;height:218px;background:var(--footer);color:#fff}
.footer h2{position:absolute;left:16px;top:10px;font-weight:400;font-size:20px}
.footer h4{position:absolute;left:16px;top:56px;font-weight:400;font-size:16px}
.footer .addr{position:absolute;left:17px;top:89px;font-size:13px;line-height:19px}
.footer .reach{position:absolute;left:214px;top:89px;font-size:13px;line-height:26px}
.quick{left:452px;top:986px;width:331px;height:195px;background:#fff;color:var(--ink)}
.quick h3{position:absolute;left:100px;top:-6px;background:#fff;padding:0 10px;font-weight:400;font-size:21px;color:var(--footer)}
.qlabel{position:absolute;font-size:15px;color:var(--footer)}
.qline{position:absolute;height:1px;background:var(--footer)}
.qbox{position:absolute;left:14px;top:120px;width:303px;height:54px;border:1.5px solid var(--footer)}
.qsubmit{position:absolute;left:0;top:175px;width:100%;text-align:center;font-size:15px;color:var(--footer)}
.copyright{left:31px;top:1187px;width:760px;height:13px;background:var(--footer-dark);color:#fff;font-size:8px;text-align:center;padding-top:1px}
</style>
</head>
<body>
<div class="canvas">

  <header>
    <div class="abs brand"><span class="brand-mark"></span><span class="brand-name">Bloom and Rise</span></div>
    <div class="abs search">SEARCH
      <svg width="10" height="10" viewBox="0 0 10 10"><circle cx="4" cy="4" r="3" fill="none" stroke="#888" stroke-width="1.2"/><line x1="6.2" y1="6.2" x2="9.2" y2="9.2" stroke="#888" stroke-width="1.4"/></svg>
    </div>
    <p class="abs tagline">“Improve you while improving someone else.”</p>
  </header>

  <nav class="abs nav">
    <span class="nav-link" style="left:27px">Home</span>
    <span class="nav-link" style="left:123px">About</span>
    <div class="nav-active"><span>Media</span></div>
    <span class="nav-link" style="left:322px">Directors &amp; Board Members</span>
    <div class="abs donate-btn">Donate</div>
  </nav>
  <div class="abs dropdown"><div>Photos</div><div class="hover">Videos</div></div>

  <div class="abs hero" role="img" aria-label="Photo of a youth soccer team in red jerseys standing together on a field"></div>
  <div class="abs hero-caption">Summer Training Program<div class="dots"><i></i><i></i><i></i><i></i><i></i></div></div>

  <section class="abs donation">
    <h2>Donation</h2>
    <span class="field-label" style="left:9px;top:44px">Amount</span>
    <div class="select" style="left:9px;top:66px;width:70px">USD<svg width="12" height="8" viewBox="0 0 12 8"><polyline points="1,1 6,6 11,1" fill="none" stroke="#333" stroke-width="1.4"/></svg></div>
    <div class="input" style="left:86px;top:66px;width:114px"></div>
    <span class="field-label" style="left:8px;top:92px">Payment Method</span>
    <div class="card" style="left:9px"><i style="background:#1a3d8f"></i></div>
    <div class="card" style="left:57px"><i style="background:#2b7fc4"></i></div>
    <div class="card" style="left:104px"><i style="background:#e45b25"></i></div>
    <div class="card" style="left:152px"><i style="background:#2a5ea8"></i></div>
    <div class="details">
      <span class="details-title">Details (Optional)</span>
      <span class="field-label" style="left:14px;top:12px">Name</span>
      <div class="select" style="left:15px;top:33px;width:57px">Mr<svg width="12" height="8" viewBox="0 0 12 8"><polyline points="1,1 6,6 11,1" fill="none" stroke="#333" stroke-width="1.4"/></svg></div>
      <div class="input" style="left:77px;top:33px;width:113px"></div>
      <span class="field-label" style="left:14px;top:57px">Email Address</span>
      <div class="input" style="left:15px;top:79px;width:176px"></div>
    </div>
    <div class="submit">Submit</div>
  </section>

  <div class="abs tab tab-news">News</div>
  <div class="abs tab tab-videos">Videos</div>
  <section class="abs videos">
    <div class="thumb thumb-a" role="img" aria-label="Video still of young players running during a soccer match">
      <div class="play"><svg width="16" height="20" viewBox="0 0 16 20"><polygon points="0,0 16,10 0,20" fill="#333"/></svg></div>
    </div>
    <div class="thumb thumb-b" role="img" aria-label="Video still of smiling youth players wearing medals">
      <div class="play"><svg width="16" height="20" viewBox="0 0 16 20"><polygon points="0,0 16,10 0,20" fill="#333"/></svg></div>
    </div>
    <span class="more">More Videos ▸</span>
  </section>

  <section class="abs events">
    <h3>Upcoming Events</h3>
    <div class="event"><small>20th Aug 2014</small><p>Vehicula libero sagittis taciti sociosqu</p></div>
    <div class="event"><small>20th Aug 2014</small><p>Vehicula libero sagittis taciti sociosqu</p></div>
    <div class="event"><small>20th Aug 2014</small><p>Vehicula libero sagittis</p></div>
    <div class="event"><small>20th Aug 2014</small><p>Vehicula libero sagittis</p></div>
    <svg class="scroll" viewBox="0 0 8 156"><polygon points="0,7 4,1 8,7" fill="#3f5f2a"/><rect x="2" y="12" width="4" height="86" fill="#3f5f2a"/><polygon points="0,150 4,156 8,150" fill="#3f5f2a"/></svg>
  </section>

  <section>
    <div class="abs about"></div>
    <div class="abs about-left"></div>
    <div class="abs about-right"></div>
    <svg class="abs" style="left:42px;top:670px" width="10" height="22" viewBox="0 0 10 22"><polygon points="0,0 10,11 0,22" fill="#3f5f2a"/></svg>
    <svg class="abs" style="left:779px;top:806px" width="10" height="22" viewBox="0 0 10 22"><polygon points="0,0 10,11 0,22" fill="#3f5f2a"/></svg>
    <p class="abs about-text"><span class="lead">We</span> are a nonprofit organization based in Des Moines, Iowa. We provides soccer training opportunities to youth soccer players looking to improve their game while also affecting the lives of the less fortunate in a positive way. While participating in the training programs the players also go out and raise money for selected charities. The organization then donates the funds. In its first 18 months we donated $10,500.</p>
    <span class="abs about-link">View Directors and Board Members</span>
    <div class="abs portrait" role="img" aria-label="Portrait photo of the organization's president"></div>
    <div class="abs person"><b>Daniel Reyes</b><span>President</span></div>
  </section>

  <section class="abs charities">
    <h2>Charities <span class="hl">Bloom and Rise</span> Donates To</h2>
    <svg class="arrow" style="left:30px" width="12" height="24" viewBox="0 0 12 24"><polygon points="12,0 0,12 12,24" fill="#f15a22"/></svg>
    <div class="charity" style="left:104px"><i></i>Open Hands</div>
    <div class="charity" style="left:242px"><i></i>Bright Path</div>
    <div class="charity" style="left:380px"><i></i>Hope Place</div>
    <div class="charity" style="left:518px"><i></i>Kind Roots</div>
    <div class="charity" style="left:652px"><i></i>Green Steps</div>
    <svg class="arrow" style="left:726px" width="12" height="24" viewBox="0 0 12 24"><polygon points="0,0 12,12 0,24" fill="#f15a22"/></svg>
  </section>

  <footer>
    <div class="abs footer">
      <h2>Contact Us</h2>
      <h4>Office Adress</h4>
      <p class="addr">Morbi viverra mauris,<br>Vitae pulvinar,<br>Tempus Mauris blandit mi</p>
      <p class="reach">Tel 5550142837<br>Email info@bloomandrise.org</p>
    </div>
    <div class="abs quick">
      <h3>Quick Contact</h3>
      <span class="qlabel" style="left:14px;top:34px">Name</span>
      <div class="qline" style="left:67px;top:52px;width:251px"></div>
      <span class="qlabel" style="left:13px;top:67px">Email Address</span>
      <div class="qline" style="left:130px;top:85px;width:188px"></div>
      <span class="qlabel" style="left:13px;top:98px">Message</span>
      <div class="qbox"></div>
      <div class="qsubmit">Submit</div>
    </div>
    <div class="abs copyright">© 2014 Bloom and Rise All rights reserved</div>
  </footer>

</div>
</body>
</html>
```